Company or website name
- Valtrix
- Links to the website
- http://prelmontlegal.example/
- Describe your company and organization and target audience
- Company secretarial and management for small business.
- The design should have the following
- The model should include :  - 5 pages. - Clean and modern design. - You must use the images are joined and make a mixture between the model of the website to respect and incorporate photos.
- Other Facts

```html
<!DOCTYPE html>
<html lang="en">
<head>
<meta charset="utf-8">
<title>Valtrix — Simple Company Secretarial Management</title>
<link rel="stylesheet" href="https://fonts.googleapis.com/css2?family=Jost:wght@200;300;400;500&family=Roboto:ital,wght@0,300;0,400;0,500;0,700;1,700&display=swap">
<style>
:root{
  --brand:#1f3b9e;
  --brand-deep:#1a3590;
  --hero:#4460b8;
  --ink:#333a4a;
  --muted:#6b6f78;
  --light:#f2f2f4;
  --white:#ffffff;
  --logo-grey:#7b7f88;
}
*{margin:0;padding:0;box-sizing:border-box}
html,body{width:1200px;height:2506px;overflow:hidden;background:var(--white)}
body{position:relative;font-family:"Roboto",sans-serif;color:var(--ink)}

/* header */
.site-header{position:absolute;left:0;top:0;width:1200px;height:96px;background:var(--white);border-bottom:2px solid #d8dbe4}
.brand{position:absolute;left:100px;top:10px;font-family:"Jost",sans-serif;font-weight:200;font-size:72px;letter-spacing:-1px;color:var(--logo-grey);line-height:1}
.main-nav a{position:absolute;top:41px;font-family:"Jost",sans-serif;font-weight:500;font-size:14.5px;letter-spacing:1.2px;color:var(--brand);text-decoration:none}
.main-nav a.is-current{color:var(--muted);border-bottom:1px solid var(--muted);padding-bottom:6px}

/* hero */
.hero{position:absolute;left:0;top:96px;width:1200px;height:548px;background:var(--hero);overflow:hidden}
.hero-photo{position:absolute;right:0;top:0;width:520px;height:548px;background:radial-gradient(ellipse at 55% 40%,#5a74c4 0%,#3a55ad 55%,#2e4899 100%)}
.hero-title{position:absolute;left:100px;top:140px;font-family:"Jost",sans-serif;font-weight:500;font-size:64px;line-height:58px;color:var(--white);letter-spacing:-.5px}
.hero-lead{position:absolute;left:98px;top:349px;font-family:"Jost",sans-serif;font-weight:400;font-size:25px;line-height:29px;color:var(--white)}
.slider-dots{position:absolute;display:flex;gap:9px}
.slider-dots span{width:12px;height:12px;border-radius:50%;background:var(--white)}

/* who we are */
.section-mark{position:absolute;height:3px;width:24px;background:var(--brand)}
.section-mark.on-dark{background:var(--white)}
.who-title{position:absolute;left:102px;top:698px;font-weight:400;font-size:41px;color:var(--brand);letter-spacing:-1px}
.who-text{position:absolute;left:102px;width:522px;font-size:15px;line-height:24px;color:var(--muted);text-align:justify;font-weight:300}
.who-photo{position:absolute;left:646px;top:692px;width:455px;height:279px;background:linear-gradient(160deg,#e6e7ea 0%,#a9acb3 55%,#4b4f58 100%)}

/* value */
.value{position:absolute;left:0;top:1015px;width:1200px;height:474px;background:var(--brand-deep);overflow:hidden}
.value-backdrop{position:absolute;left:0;top:0;width:1200px;height:474px;background:linear-gradient(90deg,#273f92 0%,#1f3b9e 40%,#1f3b9e 100%)}
.value-title{position:absolute;left:0;top:1056px;width:1200px;text-align:center;font-weight:400;font-size:40px;color:var(--white);letter-spacing:.5px}
.service{position:absolute;top:1146px;width:260px;text-align:center}
.service-disc{width:202px;height:202px;margin:0 auto;border-radius:50%;background:var(--white);display:flex;align-items:center;justify-content:center}
.service-label{margin-top:20px;font-size:19px;line-height:24px;color:var(--white);font-weight:400;letter-spacing:.3px}

/* why */
.why{position:absolute;left:0;top:1489px;width:1200px;height:497px;background:linear-gradient(110deg,#f7f7f8 0%,#efeff1 55%,#e2e3e6 100%)}
.why-title{position:absolute;left:0;top:1518px;width:1200px;text-align:center;font-weight:400;font-size:40px;color:var(--brand);letter-spacing:-1.5px}
.reason{position:absolute;width:402px}
.reason-head{display:flex;align-items:center;gap:10px;margin-left:-32px}
.reason-head svg{flex:none}
.reason-title{font-size:24px;font-weight:500;color:var(--brand);letter-spacing:-.5px;line-height:28px}
.reason-sub{font-size:16.5px;font-weight:500;color:#4a4d55;margin-top:1px;letter-spacing:-.3px}
.reason-body{margin-top:10px;font-size:15.5px;line-height:21.6px;color:#555860;letter-spacing:-.2px;font-weight:400}

/* testimonials */
.quotes{position:absolute;left:0;top:1986px;width:1200px;height:402px;background:var(--brand);overflow:hidden}
.quotes-photo{position:absolute;left:0;top:0;width:1200px;height:402px;background:linear-gradient(100deg,#1f3b9e 0%,#1f3b9e 45%,#2a459f 75%,#1c358c 100%)}
.quotes-title{position:absolute;left:0;top:2028px;width:1200px;text-align:center;font-size:40px;color:var(--white);letter-spacing:-1.5px;font-weight:400}
.quote-mark{position:absolute;font-weight:700;font-size:120px;line-height:1;color:var(--white)}
.quote{position:absolute;color:var(--white)}
.quote p{font-weight:400}
.quote cite{display:block;font-style:italic;font-weight:700}

/* footer */
.site-footer{position:absolute;left:0;top:2388px;width:1200px;height:118px;background:var(--white);border-top:3px solid #dfe1e8}
.footer-brand{position:absolute;left:100px;top:30px;font-family:"Jost",sans-serif;font-weight:200;font-size:40px;color:var(--logo-grey);letter-spacing:-1px;line-height:1}
.social{position:absolute;top:43px;display:flex;gap:32px;left:500px}
.social span{width:24px;height:24px;border-radius:50%}
.copyright{position:absolute;right:98px;top:46px;font-size:14px;color:#8a8d94;font-weight:300}
</style>
</head>
<body>

<header class="site-header">
  <div class="brand">VALTRIX</div>
  <nav class="main-nav">
    <a class="is-current" href="http://prelmontlegal.example/" style="left:486px">COMPANY</a>
    <a href="http://prelmontlegal.example/" style="left:608px">INCORPORATION</a>
    <a href="http://prelmontlegal.example/" style="left:786px">ACCOUNTING</a>
    <a href="http://prelmontlegal.example/" style="left:937px">INVESTMENT</a>
    <a href="http://prelmontlegal.example/" style="left:1085px">CONTACT</a>
  </nav>
</header>

<section class="hero">
  <div class="hero-photo" role="img" aria-label="Portrait of a smiling young businessman leaning on a desk, blue toned"></div>
  <h1 class="hero-title">SIMPLE<br>COMPANY SECRETARIAL<br>MANAGEMENT</h1>
  <p class="hero-lead">We establish and administer all forms of onshore and offshore<br>vehicles, including companies, partnerships and trusts.</p>
  <div class="slider-dots" style="left:538px;top:511px"><span></span><span></span><span></span><span></span><span></span></div>
</section>

<div class="section-mark" style="left:102px;top:690px"></div>
<h2 class="who-title">WHO WE ARE</h2>
<p class="who-text" style="top:762px">Lorem ipsum dolor sit amet, consectetur adipiscing elit. Quis est, qui non oderit libidinosam, protervam adolescentiam? Quid igitur dubitamus in tota eius natura quaerere quid sit effectum?</p>
<p class="who-text" style="top:858px">Vitae autem degendae ratio maxime quidem illis placuit quieta. Terram, mihi crede, ea lanx et maria deprimet. Si qua in iis corrigere voluit, deteriora fecit. Duo Reges: constructio interrete. Iam in altera philosophiae parte. Qua tu etiam inprudens utebare non numquam.</p>
<div class="who-photo" role="img" aria-label="Two businessmen seen from below against glass office towers"></div>

<section class="value">
  <div class="value-backdrop" role="img" aria-label="Faint close-up of a face blended with architectural blueprint lines"></div>
</section>
<div class="section-mark on-dark" style="left:382px;top:1051px"></div>
<h2 class="value-title">HOW WE DELIVER VALUE</h2>

<div class="service" style="left:75px">
  <div class="service-disc">
    <svg width="84" height="72" viewBox="0 0 84 72" fill="none" stroke="#1f3b9e" stroke-width="4" stroke-linejoin="round" stroke-linecap="round">
      <path d="M4 10 H30 L38 18 H80 V68 H4 Z"/>
      <line x1="42" y1="30" x2="42" y2="56"/><line x1="29" y1="43" x2="55" y2="43"/>
    </svg>
  </div>
  <div class="service-label">Entity formation and<br>establishment</div>
</div>
<div class="service" style="left:333px">
  <div class="service-disc">
    <svg width="78" height="78" viewBox="0 0 78 78" fill="none" stroke="#1f3b9e" stroke-width="4" stroke-linejoin="round" stroke-linecap="round">
      <rect x="4" y="12" width="70" height="62" rx="4"/>
      <line x1="4" y1="28" x2="74" y2="28"/>
      <line x1="22" y1="4" x2="22" y2="18"/><line x1="56" y1="4" x2="56" y2="18"/>
      <polyline points="26,50 35,59 53,40"/>
    </svg>
  </div>
  <div class="service-label">Annual compliance and<br>statutory maintenance</div>
</div>
<div class="service" style="left:597px">
  <div class="service-disc">
    <svg width="80" height="80" viewBox="0 0 80 80" fill="none" stroke="#1f3b9e" stroke-width="4" stroke-linejoin="round" stroke-linecap="round">
      <path d="M12 34 A28 28 0 0 1 64 22"/>
      <polyline points="66,8 66,24 50,24"/>
      <path d="M68 46 A28 28 0 0 1 16 58"/>
      <polyline points="14,72 14,56 30,56"/>
    </svg>
  </div>
  <div class="service-label">Corporate Restructuring<br>and entity rationalisation</div>
</div>
<div class="service" style="left:868px">
  <div class="service-disc">
    <svg width="120" height="120" viewBox="0 0 120 120" fill="none">
      <circle cx="60" cy="60" r="52" stroke="#1f3b9e" stroke-width="6"/>
      <circle cx="60" cy="60" r="38" fill="#1f3b9e"/>
    </svg>
  </div>
  <div class="service-label">Best practices and<br>corporate governance</div>
</div>

<section class="why" role="img" aria-label="Faint grey skyscraper facade behind the section"></section>
<div class="section-mark" style="left:460px;top:1515px"></div>
<h2 class="why-title">WHY CHOOSE US</h2>

<div class="reason" style="left:135px;top:1618px">
  <div class="reason-head"><svg width="22" height="22" viewBox="0 0 22 22" fill="none" stroke="#1f3b9e" stroke-width="2.6" stroke-linecap="round"><path d="M18 7 A8 8 0 1 1 13 3.5"/><path d="M7 11 L10.5 14.5 L19 5"/></svg><div class="reason-title">PERSONNEL QUALITY</div></div>
  <div class="reason-sub">Commitment to Quality</div>
  <p class="reason-body">The quality of our people makes us stand out. We hire the most adequate professionals. At Valtrix we set up a thorough personnel selection process and a challenging environment to grow and improve our top-notch experts.</p>
</div>
<div class="reason" style="left:700px;top:1618px">
  <div class="reason-head"><svg width="22" height="22" viewBox="0 0 22 22" fill="none" stroke="#1f3b9e" stroke-width="2.6" stroke-linecap="round"><path d="M18 7 A8 8 0 1 1 13 3.5"/><path d="M7 11 L10.5 14.5 L19 5"/></svg><div class="reason-title">EASY COMMUNICATION</div></div>
  <div class="reason-sub">Delivering Business Value</div>
  <p class="reason-body">We understand that effective communication is crucial. We establish a productive customer communication environment providing all the required resources.</p>
</div>
<div class="reason" style="left:135px;top:1812px">
  <div class="reason-head"><svg width="22" height="22" viewBox="0 0 22 22" fill="none" stroke="#1f3b9e" stroke-width="2.6" stroke-linecap="round"><path d="M18 7 A8 8 0 1 1 13 3.5"/><path d="M7 11 L10.5 14.5 L19 5"/></svg><div class="reason-title">BETTER VALUE</div></div>
  <div class="reason-sub">No Hidden Cost</div>
  <p class="reason-body">We believe all our clients deserve to enjoy higher quality services at lowest cost. So we created a business model processes combined with cloud technology to provide exactly that. All our fees are openly listed.</p>
</div>
<div class="reason" style="left:700px;top:1812px">
  <div class="reason-head"><svg width="22" height="22" viewBox="0 0 22 22" fill="none" stroke="#1f3b9e" stroke-width="2.6" stroke-linecap="round"><path d="M18 7 A8 8 0 1 1 13 3.5"/><path d="M7 11 L10.5 14.5 L19 5"/></svg><div class="reason-title">FAST RESPONSE</div></div>
  <div class="reason-sub">Time are precious to business</div>
  <p class="reason-body">Speed and accuracy are greatly valued by today businesses. We understand and value this, we strive to respond to your enquires within 1 business day.</p>
</div>

<section class="quotes">
  <div class="quotes-photo" role="img" aria-label="Raised hands giving thumbs up, blue toned"></div>
</section>
<div class="section-mark on-dark" style="left:286px;top:2022px"></div>
<h2 class="quotes-title">WHAT OUR CUSTOMERS HAVE TO SAY:</h2>

<div class="quote-mark" style="left:100px;top:2116px">“</div>
<div class="quote" style="left:168px;top:2132px;width:400px">
  <p style="font-size:15.5px;line-height:19.2px;text-indent:22px">We have been using the Valtrix to form companies for us for almost a year now and we are very impressed with the wholesale service. Companies are formed very promptly with the formation documents sent by email to us, which we then forward on to our clients so that they can set up bank accounts etc.</p>
  <cite style="margin-top:18px;font-size:15px">- Daniel Hartwell ACA FCCA CTA DMH Accountants</cite>
</div>
<div class="quote" style="left:619px;top:2130px;width:395px">
  <p style="font-size:17.5px;line-height:24px;text-indent:24px">Valtrix always provide an efficient and reliable service which is easy to use. They now handle all my Company formation requirements and I can confidently recommend them.</p>
  <cite style="margin-top:22px;font-size:16.5px">- Adrian L. Morrow, Director Briarwood Hotel</cite>
</div>
<div class="quote-mark" style="left:1054px;top:2212px">”</div>
<div class="slider-dots" style="left:552px;top:2332px;gap:17px"><span></span><span></span><span></span><span></span></div>

<footer class="site-footer">
  <div class="footer-brand">VALTRIX</div>
  <div class="social" aria-label="Social links">
    <span style="background:#3b5a98"></span>
    <span style="background:#2aa3e0"></span>
    <span style="background:#1a66a8"></span>
    <span style="background:#d8453a"></span>
  </div>
  <div class="copyright">Copyright 2016. All rights reserved.</div>
</footer>

</body>
</html>
```